依頼詳細
新規事業のランディングページのデザインをお願い致します。
シンプルで見やすく、格安でサービスを提供するという当社の強みがしっかりと伝わる、
依頼してみよう、相談してみようと感じて頂ける様なデザインを希望しています。

今回はデザインのみでコーディングは必要ございませんが、
デザインが決まりましたら、引き続きコーディングの依頼も予定しています。
サイトURL
ページ数
1ページ
希望イメージ
シンプル 複雑
単色 カラフル
暗い 明るい
日常 高級
遊び心 厳粛
未来的 伝統的
女性的 男性的
希望する色
黄・オレンジ系、緑系、青系
納品ファイル
• フォトショップ形式 (.psd)
補足説明
・ページ構成(手書きワイヤーフレーム)
・テキスト原稿(word)
・ロゴ(ai/png)
・デザイン素材(ai)
・イメージ画像(jpg)
各種資料用意していますので、文言や構成要素は統一して頂き、
レイアウトや図はデザインにより自由にご提案頂きたいです。

サイトカラーは
メインカラー→イエロー(添付のロゴカラー)
サブカラー→その他1色(自由に)
ベースカラー2色でご提案頂きたいです。
その他カラー要素はサイトカラーに合わせ、自由にご提案頂きたいです。

添付のデザイン素材内(ai)のどちらか1点(色変更あり)をデザインに組み込んで頂きたいです。
■ 選んだ理由

ページで伝えたい事をシンプルで見やすく整えて頂き、安心感を感じる点に好感を持ちました。

■ 提案者全員のお礼・コメント

今回は当社のコンペにご参加頂き誠に有難うございました。
クオリティの高いデザインをたくさんご提案頂き、当社としても有難く感じました。
また機会がありましたら利用させて頂きます。

```html
<!DOCTYPE html>
<html lang="ja">
<head>
<meta charset="utf-8">
<title>ひなた解体 | 格安内装解体</title>
<link rel="stylesheet" href="https://fonts.googleapis.com/css2?family=Noto+Serif+JP:wght@400;600;700&family=Noto+Sans+JP:wght@400;700&display=swap">
<style>
:root{
  --yellow:#f3e25c;
  --yellow-pale:#f8f3b4;
  --yellow-card:#fdf9dc;
  --ink:#2a2a2a;
  --ink-soft:#555;
  --red:#d6332b;
  --blue:#2f8fd6;
  --blue-pale:#bfe0f5;
  --rule:#cfcfcf;
  --map-land:#e4ddcd;
  --map-area:#c9703f;
  --bg:#ffffff;
}
*{box-sizing:border-box;margin:0;padding:0}
html,body{width:1200px;height:4736px;overflow:hidden;background:var(--bg)}
body{font-family:"Noto Serif JP",serif;color:var(--ink);position:relative}
.page{position:relative;width:1200px;height:4736px}
.abs{position:absolute}

.topbar{left:0;top:0;width:1200px;height:72px;background:var(--yellow-pale);display:flex;align-items:center;justify-content:center;gap:12px}
.brand{font-size:22px;font-weight:700;letter-spacing:.1em;color:#6b6320}
.brand-dot{width:16px;height:16px;border-radius:50%;background:var(--yellow)}

.hero{left:180px;top:72px;width:840px;height:888px;background:linear-gradient(160deg,#9fc3dd 0%,#d7e3ea 45%,#b9aa8f 100%)}
.hero-photo{position:absolute;inset:0}
.hero-title{position:absolute;left:0;right:0;top:150px;text-align:center;color:#fff;font-size:40px;font-weight:700;letter-spacing:.08em;text-shadow:0 2px 6px rgba(0,0,0,.45)}
.hero-sub{position:absolute;left:170px;right:170px;top:212px;text-align:center;color:#fff;font-size:18px;font-weight:600;letter-spacing:.1em;background:rgba(40,55,70,.55);padding:4px 0}
.price-tags{position:absolute;left:70px;top:280px;display:flex;gap:16px}
.price-tag{width:170px;height:110px;background:rgba(255,255,255,.9);border-top:26px solid var(--yellow);text-align:center;padding-top:18px;font-weight:700;font-size:26px;position:relative}
.price-tag span{position:absolute;top:-24px;left:0;right:0;font-size:14px}
.hero-actions{position:absolute;left:40px;top:560px;display:flex;gap:10px}
.circle-btn{width:110px;height:110px;border-radius:50%;background:var(--yellow);display:flex;flex-direction:column;align-items:center;justify-content:center;font-weight:700;font-size:24px;color:var(--ink);border:3px solid #fff;box-shadow:0 2px 6px rgba(0,0,0,.25);line-height:1.3}
.circle-btn.pale{background:var(--yellow-pale)}
.circle-btn small{font-size:14px}

.sec-title{left:180px;width:840px;text-align:center;font-size:28px;font-weight:600;letter-spacing:.1em}
.sec-title::after{content:"";display:block;width:220px;height:1px;background:var(--rule);margin:16px auto 0}
.lead{left:180px;width:840px;text-align:center;font-size:15px;line-height:1.9;color:var(--ink-soft)}

.cards{left:200px;top:1100px;width:800px;display:grid;grid-template-columns:1fr 1fr;gap:24px 28px}
.card{background:var(--yellow-card);border:2px solid var(--yellow);padding:14px 18px;height:108px;font-family:"Noto Sans JP",sans-serif;font-size:12.5px;line-height:1.7}
.card h4{font-size:14px;margin-bottom:2px}
.card .cost{text-align:right;color:var(--ink-soft)}

.banner{left:180px;top:1430px;width:840px;height:230px;background:#f2f2f2;display:flex}
.banner-photo{width:260px;height:100%;background:linear-gradient(135deg,#e0d3b8,#b8a98c)}
.banner-badge{position:absolute;left:60px;top:50px;width:130px;height:130px;border-radius:50%;background:var(--yellow);color:#fff;display:flex;align-items:center;justify-content:center;text-align:center;font-weight:700;font-size:18px;line-height:1.4;border:4px solid #fff}
.banner-body{padding:30px 30px 0 30px;font-size:15px;line-height:1.9}
.banner-body .hl{color:var(--red);font-size:22px;font-weight:700;line-height:1.5;margin-top:10px}

.secret{left:180px;width:840px;height:320px}
.secret-head{display:flex;align-items:center;gap:18px;height:90px;border-bottom:1px solid var(--rule)}
.secret-badge{width:80px;height:80px;border-radius:50%;border:3px solid var(--yellow);display:flex;align-items:center;justify-content:center;text-align:center;font-size:14px;font-weight:700;line-height:1.3;background:#fff}
.secret-name{font-size:22px;font-weight:600;letter-spacing:.1em}
.secret-catch{margin-left:auto;font-size:34px;font-weight:700;letter-spacing:.08em}
.secret-catch.small{font-size:20px}
.secret-body{display:flex;gap:28px;margin-top:22px}
.secret-photo{width:380px;height:190px;flex:none}
.secret-text{font-family:"Noto Sans JP",sans-serif;font-size:13.5px;line-height:1.9;color:var(--ink-soft)}
.secret-text .red{color:var(--red)}

.compare{left:180px;top:3090px;width:840px;height:380px}
.compare h3{text-align:center;font-size:36px;font-weight:700;letter-spacing:.1em}
.compare-figure{width:480px;height:290px;margin:18px auto 0;background:linear-gradient(90deg,var(--blue) 0%,var(--blue-pale) 50%,#ffffff 52%,var(--blue-pale) 70%,var(--blue) 100%)}

.area-text{left:180px;top:3560px;width:840px;text-align:center;font-family:"Noto Sans JP",sans-serif;font-size:13px;line-height:1.9}
.area-map{left:180px;top:3760px;width:840px;height:540px;background:
  radial-gradient(ellipse 230px 150px at 42% 30%,var(--map-area) 0%,rgba(201,112,63,.75) 55%,rgba(201,112,63,0) 100%),
  radial-gradient(ellipse 300px 180px at 32% 55%,rgba(214,140,95,.8) 0%,rgba(214,140,95,0) 100%),
  linear-gradient(120deg,var(--map-land) 0%,#d8cfb8 60%,var(--map-land) 100%)}

.cta-title{left:180px;top:4340px;width:840px;text-align:center;font-size:36px;font-weight:700;line-height:1.45;letter-spacing:.06em}
.cta-actions{left:0;top:4470px;width:1200px;display:flex;justify-content:center;gap:24px}
.cta-actions .circle-btn{width:120px;height:120px;font-size:26px;border:none;box-shadow:none}
.hours{left:0;top:4612px;width:1200px;text-align:center;font-family:"Noto Sans JP",sans-serif;font-size:13px}
.footer{left:0;top:4668px;width:1200px;height:68px;border-top:1px solid var(--rule);display:flex;align-items:center;justify-content:center;font-size:14px;gap:10px}
</style>
</head>
<body>
<div class="page">

  <header class="abs topbar">
    <span class="brand-dot"></span><span class="brand">ひなた解体</span>
  </header>

  <section class="abs hero">
    <div class="hero-photo" role="img" aria-label="解体工事現場とヘルメットを手に笑顔の作業服の男性の写真"></div>
    <h1 class="hero-title">格安で高品質・スピーディーな内装解体を</h1>
    <p class="hero-sub">経費を徹底的に見直し、適正価格でご提供します</p>
    <div class="price-tags">
      <div class="price-tag"><span>スケルトン</span>¥7,000〜/坪</div>
      <div class="price-tag"><span>原状回復</span>¥5,000〜/坪</div>
    </div>
    <div class="hero-actions">
      <div class="circle-btn">費用例</div>
      <div class="circle-btn">電話</div>
      <div class="circle-btn pale"><small>LINE</small>無料相談</div>
    </div>
  </section>

  <h2 class="abs sec-title" style="top:1000px">内装解体工事費用例</h2>
  <p class="abs lead" style="top:1050px;font-size:13px">実際の施工例をもとにした費用の目安です。現地調査のうえ正式なお見積りをお出しします。</p>
  <div class="abs cards">
    <div class="card"><h4>費用例1</h4>飲食店 約30坪 スケルトン解体<br>厨房設備・内装材の撤去、産廃処分<br><p class="cost">合計 約210,000円（税別）</p></div>
    <div class="card"><h4>費用例2</h4>事務所 約45坪 原状回復工事<br>間仕切り・床材撤去、天井ボード撤去<br><p class="cost">合計 約230,000円（税別）</p></div>
    <div class="card"><h4>費用例3</h4>美容室 約20坪 スケルトン解体<br>設備撤去・内装撤去、産廃処分<br><p class="cost">合計 約150,000円（税別）</p></div>
    <div class="card"><h4>費用例4</h4>物販店 約35坪 原状回復工事<br>什器・床材撤去、クロス剥がし<br><p class="cost">合計 約180,000円（税別）</p></div>
  </div>

  <h2 class="abs sec-title" style="top:1356px">解体工事の費用は大きく分けて3つ</h2>
  <div class="abs banner">
    <div class="banner-photo" role="img" aria-label="作業現場の写真"></div>
    <div class="banner-badge">当社の<br>格安の秘訣</div>
    <div class="banner-body">
      <p>人件費・ゴミ処分費・諸経費の3つで構成されています。<br>一般的な業者は余計な中間マージンや経費が上乗せされます。</p>
      <p class="hl">当社ではこれらにかかる費用をカットする事で<br>格安での工事を実現いたします！</p>
    </div>
  </div>

  <section class="abs secret" style="top:1720px">
    <div class="secret-head"><div class="secret-badge">秘訣<br>其の1</div><span class="secret-name">ゴミのカット</span><span class="secret-catch">産業廃棄物を削減</span></div>
    <div class="secret-body">
      <div class="secret-photo" role="img" aria-label="袋詰めされた産業廃棄物の写真" style="background:linear-gradient(135deg,#8f9a8c,#4f5a52)"></div>
      <p class="secret-text">解体工事で最も費用がかかるのが廃棄物の処分費です。当社では分別を徹底し、処分量そのものを減らしています。<br><span class="red">分別作業を現場で行うことで、処分費を大幅に抑えることができます。</span><br>無駄なゴミを出さない工夫が格安の秘訣です。</p>
    </div>
  </section>

  <section class="abs secret" style="top:2055px">
    <div class="secret-head"><div class="secret-badge">秘訣<br>其の2</div><span class="secret-name">リサイクル活用</span><span class="secret-catch">利益を還元</span></div>
    <div class="secret-body">
      <div class="secret-photo" role="img" aria-label="再利用できる木材や資材の写真" style="background:linear-gradient(135deg,#d9c4a0,#9c7f55)"></div>
      <p class="secret-text">撤去した什器や資材のうち、再利用できるものはリサイクルに回します。<br>そこで得た利益をお客様の工事費用に還元しています。<br><span class="red">リサイクル業者との直接取引で、さらに費用を下げることが可能です。</span></p>
    </div>
  </section>

  <section class="abs secret" style="top:2390px">
    <div class="secret-head"><div class="secret-badge">秘訣<br>其の3</div><span class="secret-name">中間マージンのカット</span><span class="secret-catch small">不要なマージンが発生しています</span></div>
    <div class="secret-body">
      <div class="secret-photo" role="img" aria-label="元請けから下請けへ工事が流れる構造のイラスト" style="background:linear-gradient(135deg,#f4eec8,#cfc58f)"></div>
      <p class="secret-text">一般的な解体工事は元請けから下請け、孫請けへと発注され、そのたびにマージンが上乗せされます。<br><span class="red">当社は自社施工のため中間マージンが一切かかりません。</span><br>その分を価格に反映しています。</p>
    </div>
  </section>

  <section class="abs secret" style="top:2725px">
    <div class="secret-head"><div class="secret-badge">秘訣<br>其の4</div><span class="secret-name">オンライン活用</span><span class="secret-catch small">見えない経費が発生しています</span></div>
    <div class="secret-body">
      <div class="secret-photo" role="img" aria-label="パソコンに向かいヘッドセットで対応するスタッフの写真" style="background:linear-gradient(135deg,#e7edf2,#a9b8c4)"></div>
      <p class="secret-text">営業担当の訪問や店舗運営には多くの経費がかかります。当社はお問い合わせやお見積りをオンラインで行い、<br><span class="red">営業経費や店舗コストを削減しています。</span><br>LINEや電話でお気軽にご相談いただけます。</p>
    </div>
  </section>

  <section class="abs compare">
    <h3>当社では</h3>
    <div class="compare-figure" role="img" aria-label="一般的な業者と当社の費用構成を比べ、諸経費を約50%カットできることを示す図"></div>
  </section>

  <h2 class="abs sec-title" style="top:3480px">対応エリア</h2>
  <div class="abs area-text">
    <p>東京都全域</p>
    <p>港区・千代田区・中央区・新宿区・渋谷区・品川区・目黒区・大田区・世田谷区 ほか23区</p>
    <p>八王子市・町田市・府中市・調布市 ほか多摩地域</p>
    <p>神奈川県全域</p>
    <p>横浜市・川崎市・相模原市・藤沢市 ほか</p>
  </div>
  <div class="abs area-map" role="img" aria-label="東京都と神奈川県の対応エリアを色分けした地図"></div>

  <h2 class="abs cta-title">まずは気軽に<br>LINEや電話でご相談ください</h2>
  <div class="abs cta-actions">
    <div class="circle-btn">費用例</div>
    <div class="circle-btn">電話</div>
    <div class="circle-btn pale" style="font-size:16px"><span>LINE</span><span>無料相談</span></div>
  </div>
  <p class="abs hours">営業時間 10:00〜18:00（土・日・祝除く）</p>
  <footer class="abs footer"><span>ひなた解体</span><span>|</span><span>会社概要</span></footer>

</div>
</body>
</html>
```